Flyer for the Radiant Harvest Worship Day 2020

I am looking to create a flyer for a one day prayer retreat our church is organizing.
This flyer will be posted on social media, websites and will also be printed so it can be mailed to people.
I am looking for something professional, with good use of our logo and band colors (logo colors).
I am counting on the designer's skill, creativity, art and knowledge of media communication to produce a flyer that will effectively and quickly convey the message we are trying to spread.
CONTENT OF THE FLYER:
Event title: Radiant Harvest Worship Day
Date: Tuesday July 2nd, 2020
Time: 11:00AM - 7:00PM
Maplewood Hotel, 4817 Birchfield Avenue, Portland, Maine 04109 (Room: Evergreen)
Event Key words to highlight what the event is about: Prayer, Sharing the Word, Panel discussion, prophecy, Impartation.
Key phrases:
A one day prayer retreat.
Jesus Chris is Lord
Contact info:
www.tolvex.org
Phone: 207 555 0143
Email: contact@brookmeadow.org

```html
<!DOCTYPE html>
<html lang="en">
<head>
<meta charset="utf-8">
<title>Radiant Harvest Worship Day</title>
<link href="https://fonts.googleapis.com/css2?family=Catamaran:wght@300;400;700;800;900&display=swap" rel="stylesheet">
<style>
  :root{
    --navy:#173a63;
    --orange:#f7941d;
    --white:#ffffff;
    --page:#f2f3f5;
    --sky-top:#f4f1ea;
    --sky-mid:#e9e6dd;
    --crowd:#b9c3d6;
    --crowd-deep:#9eacc6;
  }
  *{margin:0;padding:0;box-sizing:border-box}
  html,body{width:1200px;height:572px;overflow:hidden;background:var(--page)}
  body{font-family:"Catamaran",sans-serif;position:relative}

  .flyer{position:absolute;left:330px;top:16px;width:540px;height:540px;overflow:hidden;background:var(--white);box-shadow:0 1px 4px rgba(0,0,0,.12)}
  .flyer__photo{position:absolute;left:0;top:0;width:540px;height:459px;
    background:linear-gradient(180deg,var(--sky-top) 0%,var(--sky-mid) 40%,var(--crowd) 75%,var(--crowd-deep) 100%)}

  .ribbon{position:absolute}
  .ribbon svg{position:absolute;left:0;top:0}
  .ribbon__label{position:absolute;left:0;width:100%;text-align:center;color:var(--white);font-weight:800}

  .title-ribbon{left:87px;top:21px;width:366px;height:50px}
  .title-ribbon .ribbon__label{top:5px;font-size:24px;line-height:30px;letter-spacing:.1px}

  .tagline{position:absolute;left:0;width:540px;text-align:center;font-style:italic;font-weight:900;font-size:14.5px;line-height:16px}
  .tagline--retreat{top:80px;color:var(--orange)}
  .tagline--lord{top:97px;color:var(--navy)}

  .section-ribbon{left:205px;width:130px;height:32px}
  .section-ribbon .ribbon__label{top:2px;font-size:18px;line-height:24px}
  .section-ribbon--when{top:133px}
  .section-ribbon--where{top:218px}

  .event-date{position:absolute;left:54px;top:183px;font-size:15.5px;font-weight:700;color:var(--navy)}
  .event-time{position:absolute;left:351px;top:180px;font-size:15.5px;font-weight:700;color:var(--orange)}

  .venue{position:absolute;left:0;top:272px;width:540px;text-align:center;font-size:15.5px;line-height:18.5px;font-weight:700;color:var(--navy)}

  .topics{position:absolute;left:0;top:341px;width:540px;height:80px}
  .topic{position:absolute;top:0;width:80px;height:80px;margin-left:-40px;border-radius:50%;background:var(--white);
    display:flex;align-items:center;justify-content:center;text-align:center;color:var(--orange);font-weight:400;font-size:14px;line-height:15px}

  .footer{position:absolute;left:0;top:459px;width:540px;height:81px;display:flex}
  .footer__brand{width:122px;background:var(--white);display:flex;align-items:center;justify-content:center;gap:5px}
  .brand-dot{width:9px;height:9px;border-radius:50%;background:var(--orange)}
  .brand-name{font-weight:700;font-size:22px;color:var(--navy);letter-spacing:.5px}
  .footer__contact{flex:1;background:var(--orange);position:relative;color:var(--white)}
  .contact-row{position:absolute;left:16px;display:flex;align-items:center;gap:14px;font-size:15px;font-weight:700}
  .contact-row--web{top:8px}
  .contact-row--mail{top:41px}
  .contact-icon{width:25px;height:25px;border-radius:50%;background:var(--white);display:flex;align-items:center;justify-content:center}
  .call{position:absolute;right:20px;text-align:right;font-weight:800}
  .call--label{top:6px;font-size:21px;color:var(--white);letter-spacing:.5px}
  .call--number{top:38px;font-size:21px;color:var(--navy)}
</style>
</head>
<body>
  <main class="flyer">
    <div class="flyer__photo" role="img" aria-label="Photo of a group of smiling young people sitting together outdoors under trees, softly faded"></div>

    <div class="ribbon title-ribbon">
      <svg width="366" height="50" viewBox="0 0 366 50">
        <polygon points="0,8 24,8 24,50 12,29" fill="var(--navy)"/>
        <polygon points="366,8 342,8 342,50 354,29" fill="var(--navy)"/>
        <rect x="14" y="0" width="338" height="40" fill="var(--navy)"/>
      </svg>
      <div class="ribbon__label">Radiant Harvest Worship Day</div>
    </div>

    <p class="tagline tagline--retreat">A one day prayer retreat</p>
    <p class="tagline tagline--lord">Jesus Christ is Lord</p>

    <div class="ribbon section-ribbon section-ribbon--when">
      <svg width="130" height="32" viewBox="0 0 130 32">
        <polygon points="0,6 14,6 14,32 6,19" fill="var(--orange)"/>
        <polygon points="130,6 116,6 116,32 124,19" fill="var(--orange)"/>
        <rect x="8" y="0" width="114" height="27" fill="var(--orange)"/>
      </svg>
      <div class="ribbon__label">When?</div>
    </div>

    <p class="event-date">Tuesday July 2nd, 2020</p>
    <p class="event-time">11:00AM - 7:00PM</p>

    <div class="ribbon section-ribbon section-ribbon--where">
      <svg width="130" height="32" viewBox="0 0 130 32">
        <polygon points="0,6 14,6 14,32 6,19" fill="var(--orange)"/>
        <polygon points="130,6 116,6 116,32 124,19" fill="var(--orange)"/>
        <rect x="8" y="0" width="114" height="27" fill="var(--orange)"/>
      </svg>
      <div class="ribbon__label">Where?</div>
    </div>

    <p class="venue">Maplewood Hotel, 4817 Birchfield Avenue,<br>Portland, Maine 04109 (Room: Evergreen)</p>

    <ul class="topics">
      <li class="topic" style="left:75px">Prayer</li>
      <li class="topic" style="left:173px">Sharing<br>the Word</li>
      <li class="topic" style="left:269px">Panel<br>discussion</li>
      <li class="topic" style="left:371px">Impartation</li>
      <li class="topic" style="left:467px">Prophecy</li>
    </ul>

    <footer class="footer">
      <div class="footer__brand">
        <span class="brand-dot"></span>
        <span class="brand-name">TOLVEX</span>
      </div>
      <div class="footer__contact">
        <div class="contact-row contact-row--web">
          <span class="contact-icon">
            <svg width="14" height="14" viewBox="0 0 14 14" fill="none" stroke="var(--orange)" stroke-width="1.8" stroke-linecap="round">
              <path d="M6 8 L8 6"/>
              <path d="M5 6.5 L3.3 8.2 a2 2 0 0 0 2.8 2.8 L7.5 9.3"/>
              <path d="M9 7.5 L10.7 5.8 a2 2 0 0 0 -2.8 -2.8 L6.5 4.7"/>
            </svg>
          </span>
          <span>www.tolvex.org</span>
        </div>
        <div class="contact-row contact-row--mail">
          <span class="contact-icon">
            <svg width="14" height="11" viewBox="0 0 14 11" fill="none" stroke="var(--orange)" stroke-width="1.5">
              <rect x="1" y="1" width="12" height="9"/>
              <path d="M1 1 L7 6 L13 1"/>
            </svg>
          </span>
          <span>contact@brookmeadow.org</span>
        </div>
        <p class="call call--label">CALL NOW!</p>
        <p class="call call--number">207 555 0143</p>
      </div>
    </footer>
  </main>
</body>
</html>
```